Construction Company Business Card

Business Card Design using new Logo

Contact Information for Business Card

include all company info and website

Requirements
Must have
• Wesley Corman - President
ph. 254-617-0382
Cedar Knoll, TX
wesley@ironmarkframing.com
www.ironmarkframing.com

```html
<!DOCTYPE html>
<html lang="en">
<head>
<meta charset="utf-8">
<title>Ironmark Framing – Business Card</title>
<link href="https://fonts.googleapis.com/css2?family=Poppins:wght@400;500;600&display=swap" rel="stylesheet">
<style>
  :root {
    --navy: #0a2249;
    --red: #c8353a;
    --white: #ffffff;
    --soft-white: #e9edf4;
    --page: #ffffff;
  }
  * { margin: 0; padding: 0; box-sizing: border-box; }
  html, body { width: 1200px; height: 1200px; overflow: hidden; background: var(--page); }
  body { position: relative; font-family: "Poppins", sans-serif; color: var(--white); }

  .card {
    position: absolute;
    left: 216px;
    width: 775px;
    height: 431px;
    background: var(--navy);
  }
  .card--front { top: 152px; }
  .card--back { top: 625px; }

  .brand-name {
    position: absolute;
    font-weight: 500;
    color: var(--white);
    white-space: nowrap;
    transform: translate(-50%, -50%);
    letter-spacing: 1px;
    display: flex;
    align-items: center;
    gap: 10px;
  }
  .brand-name .brand-dot {
    width: 12px; height: 12px; border-radius: 50%;
    background: var(--red);
    flex: none;
  }
  .card--front .brand-name { left: 387px; top: 201px; font-size: 28px; }
  .card--back .brand-name { left: 198px; top: 206px; font-size: 23px; }

  .front-url {
    position: absolute;
    left: 0; right: 0; top: 384px;
    display: flex; align-items: center; justify-content: center;
    gap: 6px;
    font-size: 21px; font-weight: 500;
    letter-spacing: 8.2px;
  }
  .front-url .rule {
    height: 1px; width: 160px;
    background: linear-gradient(90deg, rgba(255,255,255,0), rgba(255,255,255,0.35));
  }
  .front-url .rule--right {
    background: linear-gradient(90deg, rgba(255,255,255,0.35), rgba(255,255,255,0));
  }

  .back-divider {
    position: absolute; left: 390px; top: 101px;
    width: 2px; height: 228px; background: var(--red);
  }
  .person-name {
    position: absolute; left: 421px; top: 94px;
    font-size: 24px; font-weight: 600; letter-spacing: 2.6px;
    white-space: nowrap;
  }
  .person-name .first { color: var(--red); }
  .person-name .last { color: var(--white); }
  .person-title {
    position: absolute; left: 421px; top: 132px;
    font-size: 14px; font-weight: 500; letter-spacing: 4px;
  }
  .title-rule {
    position: absolute; left: 421px; top: 163px;
    width: 208px; height: 1px;
    background: linear-gradient(90deg, rgba(255,255,255,0.3), rgba(255,255,255,0));
  }

  .contact-list { position: absolute; left: 421px; top: 190px; list-style: none; }
  .contact-item {
    display: flex; align-items: center; gap: 14px;
    height: 28px; margin-bottom: 8px;
    font-size: 17px; color: var(--soft-white);
    white-space: nowrap;
  }
  .contact-icon { width: 28px; height: 28px; flex: none; }
</style>
</head>
<body>

<section class="card card--front">
  <div class="brand-name"><span class="brand-dot"></span>IRONMARK FRAMING</div>
  <div class="front-url">
    <span class="rule"></span>
    <span>www.ironmarkframing.com</span>
    <span class="rule rule--right"></span>
  </div>
</section>

<section class="card card--back">
  <div class="brand-name"><span class="brand-dot"></span>IRONMARK FRAMING</div>

  <div class="back-divider"></div>

  <h1 class="person-name"><span class="first">WESLEY</span> <span class="last">CORMAN</span></h1>
  <p class="person-title">PRESIDENT</p>
  <div class="title-rule"></div>

  <ul class="contact-list">
    <li class="contact-item">
      <svg class="contact-icon" viewBox="0 0 28 28" aria-hidden="true">
        <circle cx="14" cy="14" r="12.5" fill="#fff" stroke="#c8353a" stroke-width="2.5"/>
        <path d="M9.5 8.5c.8-.8 1.6-.6 2 .1l1.1 2c.3.6.1 1.1-.4 1.5l-.7.5c.6 1.5 1.8 2.8 3.3 3.5l.5-.7c.4-.5 1-.6 1.5-.3l2 1.1c.7.4.8 1.3.1 2-1 1-2.3 1.2-3.6.6-3-1.4-5-3.6-6.3-6.4-.6-1.3-.4-2.3.5-2.9z" fill="#c8353a"/>
      </svg>
      <span>254-617-0382</span>
    </li>
    <li class="contact-item">
      <svg class="contact-icon" viewBox="0 0 28 28" aria-hidden="true">
        <circle cx="14" cy="14" r="12.5" fill="#fff" stroke="#c8353a" stroke-width="2.5"/>
        <rect x="7.5" y="9.5" width="13" height="9" fill="#c8353a"/>
        <path d="M7.5 9.5l6.5 5 6.5-5M7.5 18.5l5-4.2M20.5 18.5l-5-4.2" stroke="#fff" stroke-width="1" fill="none"/>
      </svg>
      <span>wesley@ironmarkframing.com</span>
    </li>
    <li class="contact-item">
      <svg class="contact-icon" viewBox="0 0 28 28" aria-hidden="true">
        <circle cx="14" cy="14" r="12.5" fill="#fff" stroke="#c8353a" stroke-width="2.5"/>
        <g fill="none" stroke="#c8353a" stroke-width="1">
          <circle cx="14" cy="14" r="6.5"/>
          <ellipse cx="14" cy="14" rx="3" ry="6.5"/>
          <path d="M7.5 14h13M8.5 10.8h11M8.5 17.2h11M14 7.5v13"/>
        </g>
      </svg>
      <span>www.ironmarkframing.com</span>
    </li>
    <li class="contact-item">
      <svg class="contact-icon" viewBox="0 0 28 28" aria-hidden="true">
        <circle cx="14" cy="14" r="12.5" fill="#fff" stroke="#c8353a" stroke-width="2.5"/>
        <path d="M14 21.5s-5-5.3-5-9a5 5 0 0 1 10 0c0 3.7-5 9-5 9z" fill="#c8353a"/>
        <circle cx="14" cy="12.3" r="1.8" fill="#fff"/>
      </svg>
      <span>Cedar Knoll, TX.</span>
    </li>
  </ul>
</section>

</body>
</html>
```